Texting While Driving/Distracted Driving Educational Poster

We are a design-driven nutrition, health, and wellness educational company looking for a fresh, eye-catching educational poster design to promote attentive driving, primarily to young and new drivers. Young, inexperienced drivers (under 20) have the highest proportion of distraction-related fatal crashes, with talking and texting being the most commonly recognized distraction. We hope to draw attention to this issue with an engaging, persuasive poster. The poster will be printed and available for purchase on our website and print catalogs.

Target Market(s)

The audience is American teen to adult drivers and the buyer is educators and healthcare professionals.

Requirements
Must have
• The poster must be 18" x 24" trim size, all fonts in outlines, full color art converted to CMYK.

```html
<!DOCTYPE html>
<html lang="en">
<head>
<meta charset="utf-8">
<title>Focus On d Road – Public Interest Poster</title>
<link rel="stylesheet" href="https://fonts.googleapis.com/css2?family=Anton&family=Arimo:wght@400;700&family=Open+Sans:wght@700&display=swap">
<style>
  :root {
    --page: #ffffff;
    --page-edge: #a6a6a6;
    --frame-red: #ff0000;
    --poster-black: #000000;
    --text-white: #ffffff;
    --mark-grey: #a6a6a6;
  }
  * { margin: 0; padding: 0; box-sizing: border-box; }
  html, body {
    width: 1200px;
    height: 900px;
    overflow: hidden;
    background: var(--page);
  }
  .canvas {
    position: relative;
    width: 1200px;
    height: 900px;
    border: 1px solid var(--page-edge);
    background: var(--page);
  }
  .poster {
    position: absolute;
    left: 263px;
    top: 0;
    width: 674px;
    height: 900px;
    background: var(--frame-red);
  }
  .poster-field {
    position: absolute;
    left: 19px;
    top: 18px;
    width: 637px;
    height: 862px;
    background: var(--poster-black);
  }
  .headline {
    position: absolute;
    left: 0;
    top: 0;
    width: 637px;
    height: 460px;
  }
  .headline-word {
    font-family: "Anton", "Impact", sans-serif;
    fill: var(--frame-red);
  }
  .headline-mark {
    fill: var(--mark-grey);
  }
  .teaser {
    position: absolute;
    left: 0;
    top: 548px;
    width: 637px;
    text-align: center;
    font-family: "Open Sans", sans-serif;
    font-weight: 700;
    font-size: 13px;
    color: var(--text-white);
  }
  .message {
    position: absolute;
    left: 0;
    top: 642px;
    width: 637px;
    text-align: center;
    font-family: "Arimo", sans-serif;
    font-weight: 400;
    font-size: 37px;
    color: var(--text-white);
  }
  .message strong { font-weight: 700; }
  .footnote {
    position: absolute;
    right: 9px;
    bottom: 7px;
    font-family: "Arimo", sans-serif;
    font-size: 12px;
    color: var(--text-white);
  }
</style>
</head>
<body>
  <main class="canvas">
    <section class="poster">
      <div class="poster-field">
        <svg class="headline" viewBox="0 0 637 460" aria-label="SEX">
          <text class="headline-word" x="46" y="422" font-size="452" textLength="516" lengthAdjust="spacingAndGlyphs">SEX</text>
          <polygon class="headline-mark" points="590,65 597,72 605,70 604,80 610,87 601,91 598,100 590,94 582,100 579,91 570,87 576,80 575,70 583,72"/>
        </svg>
        <p class="teaser">OKAY so we got your attention, here’s the msg</p>
        <p class="message">“<strong>Focus</strong> On d <strong>Road</strong>”</p>
        <p class="footnote">* Issued in public interest. Yes, No Sex</p>
      </div>
    </section>
  </main>
</body>
</html>
```